依頼詳細
当サイトに店舗情報等を掲載してもらうための店舗への説明用チラシのデザイン制作をお願い致します。思わず掲載をしたくなるようなデザインをお願いします。シンプルでわかり易いものが希望です。
記載項目
サイト名はsemu(セム)・店舗情報掲載料1P21,000円/年額 複数P(写真・メニュー・クーポン等)42,000円/年額 求人情報掲載無料・採用時31,500円 当サイトの収益は児童養護施設等の子供達の学習支援に使われます。
サイズ
A4
ページ数
片面
希望イメージ
シンプル 複雑
単色 カラフル
暗い 明るい
日常 高級
遊び心 厳粛
未来的 伝統的
女性的 男性的
希望する色
オレンジ
納品ファイル
• 高解像度JPG (.jpg)
• イラストレーター形式 (.ai)
補足説明
《選ぶワクワクを全ての人に》をミッションにしたNPOです。この度開設するサイトを通じて、大人の生活の選択肢を増やし、学習支援によって子どもの将来の選択肢を増やすことを目的としています。サイト開設にあたっては、一定数の店舗登録が必須なため、店舗への説明がわかりやすい営業用チラシが必要です。イメージとしてはひらけ堂やぽみたすが近いかと思います。

```html
<!DOCTYPE html>
<html lang="ja">
<head>
<meta charset="utf-8">
<title>SEMU 店舗掲載のご案内</title>
<link rel="stylesheet" href="https://fonts.googleapis.com/css2?family=Noto+Sans+JP:wght@400;500;700;900&family=M+PLUS+Rounded+1c:wght@500;700;800&display=swap">
<style>
:root{
  --orange:#f28b1e;
  --orange-deep:#e9691c;
  --cream:#fde9c4;
  --ink:#333333;
  --grey:#6b6b6b;
  --panel:#ededed;
  --panel-dark:#5a5a5a;
  --map:#f7d3dc;
  --map-soft:#fbe3e9;
  --event:#f5a623;
  --gourmet:#e0443c;
  --useful:#b24b9b;
  --beauty:#8fcf4f;
  --work:#2fae6a;
  --center:#f7d51e;
  --line:#9a9a9a;
}
*{margin:0;padding:0;box-sizing:border-box}
html,body{width:849px;height:1200px;overflow:hidden;background:#fff}
body{font-family:"Noto Sans JP",sans-serif;color:var(--ink);position:relative}
.header{position:absolute;left:0;top:0;width:849px;height:78px;background:var(--orange)}
.brand{position:absolute;left:22px;top:4px;font-weight:900;font-size:46px;color:#fff;letter-spacing:1px;line-height:1}
.tagline{position:absolute;left:300px;top:12px;width:530px;height:38px;background:#fff;color:var(--orange);font-weight:700;font-size:21px;display:flex;align-items:center;justify-content:center;letter-spacing:1px}
.site-url{position:absolute;left:22px;top:56px;font-size:12px;color:#fff}
.hero{position:absolute;left:0;top:78px;width:849px;height:730px}
.hero svg{position:absolute;left:0;top:0}
.circle-label{font-family:"M PLUS Rounded 1c",sans-serif;font-weight:800;fill:#fff;text-anchor:middle}
.circle-sub{font-family:"Noto Sans JP",sans-serif;font-size:9px;fill:#fff;text-anchor:middle;letter-spacing:.5px}
.catch-band{position:absolute;left:690px;top:0;width:34px;height:340px;background:var(--cream)}
.catch-sub{position:absolute;left:696px;top:10px;writing-mode:vertical-rl;font-size:17px;font-weight:500;color:var(--ink);letter-spacing:2px}
.catch-main{position:absolute;left:762px;top:4px;writing-mode:vertical-rl;font-size:46px;font-weight:900;color:var(--orange-deep);letter-spacing:1px;line-height:1}
.note{position:absolute;left:22px;top:815px;width:805px;border-top:1px solid #ccc;padding-top:6px;font-size:13px;font-weight:700;color:var(--orange-deep)}
.note::before{content:"";display:inline-block;width:9px;height:9px;background:var(--orange);margin-right:6px}
.fees{position:absolute;left:22px;top:848px;width:268px;height:318px;background:var(--panel)}
.fees h2{background:var(--panel-dark);color:#fff;font-size:16px;font-weight:700;text-align:center;padding:5px 0;letter-spacing:3px}
.fees .body{padding:12px 14px;font-size:12.5px;line-height:1.75}
.fees h3{font-size:14px;font-weight:700;margin-bottom:4px}
.fees .contact{margin-top:12px}
.about{position:absolute;left:304px;top:848px;width:240px;height:318px}
.about h2{font-size:18px;font-weight:700;border-bottom:2px solid var(--ink);padding-bottom:4px;margin-bottom:10px}
.about p{font-size:12px;line-height:1.75;color:var(--grey)}
.about .address{margin-top:14px;color:var(--ink)}
.screens{position:absolute;left:560px;top:848px;width:268px;height:318px}
.screen{position:absolute;border:1px solid #ccc}
.footer{position:absolute;left:0;top:1180px;width:849px;height:20px;background:var(--orange)}
</style>
</head>
<body>
<header class="header">
  <div class="brand">SEMU</div>
  <div class="tagline">八代市お出かけ情報ポータルサイト</div>
  <div class="site-url">サイトURL ｜ http://www.semu.or.jp</div>
</header>

<section class="hero">
  <div class="catch-band"></div>
  <div class="catch-sub">セムから広がる新たな八代ライフ</div>
  <div class="catch-main">八代市のワクワクを全ての人に。</div>

  <svg width="690" height="730" viewBox="0 0 690 730">
    <defs>
      <linearGradient id="mapFill" x1="0" y1="0" x2="0" y2="1">
        <stop offset="0" stop-color="var(--map-soft)"/>
        <stop offset="1" stop-color="var(--map)"/>
      </linearGradient>
    </defs>
    <rect role="img" aria-label="八代市の地図" x="20" y="120" width="620" height="570" rx="40" fill="url(#mapFill)"/>
    <rect role="img" aria-label="スマートフォン" x="470" y="50" width="34" height="60" rx="5" fill="#b9b9b9"/>
    <rect role="img" aria-label="スマートフォン" x="600" y="250" width="30" height="56" rx="5" fill="#b9b9b9"/>
    <rect role="img" aria-label="タブレット" x="200" y="90" width="60" height="80" rx="6" fill="#c9c9c9"/>
    <rect role="img" aria-label="ノートパソコン" x="150" y="620" width="100" height="66" rx="4" fill="#c9c9c9"/>
    <g stroke="var(--line)" stroke-width="2">
      <line x1="290" y1="390" x2="115" y2="225"/>
      <line x1="290" y1="390" x2="430" y2="175"/>
      <line x1="290" y1="390" x2="100" y2="490"/>
      <line x1="290" y1="390" x2="545" y2="380"/>
      <line x1="290" y1="390" x2="340" y2="590"/>
    </g>
    <circle cx="290" cy="390" r="92" fill="#fff"/>
    <circle cx="290" cy="390" r="84" fill="var(--center)"/>
    <text x="290" y="405" class="circle-label" font-size="40">セム</text>

    <circle cx="115" cy="225" r="56" fill="var(--event)"/>
    <text x="115" y="228" class="circle-label" font-size="15">たのしむ</text>
    <text x="115" y="244" class="circle-sub">EVENT</text>

    <circle cx="430" cy="175" r="56" fill="var(--gourmet)"/>
    <text x="430" y="182" class="circle-label" font-size="15">ごちそう</text>
    <text x="430" y="198" class="circle-sub">GOURMET</text>

    <circle cx="100" cy="490" r="56" fill="var(--useful)"/>
    <text x="100" y="493" class="circle-label" font-size="14">おやくだち</text>
    <text x="100" y="509" class="circle-sub">USEFUL</text>

    <circle cx="545" cy="380" r="52" fill="var(--beauty)"/>
    <text x="545" y="383" class="circle-label" font-size="13">きれいになる</text>
    <text x="545" y="399" class="circle-sub">BEAUTIFUL</text>

    <circle cx="340" cy="590" r="56" fill="var(--work)"/>
    <text x="340" y="593" class="circle-label" font-size="15">はたらく</text>
    <text x="340" y="609" class="circle-sub">WORK</text>
  </svg>
</section>

<p class="note">当サイトの収益は児童養護施設等の子供達の学習支援に使われます。</p>

<section class="fees">
  <h2>掲載店舗募集中</h2>
  <div class="body">
    <h3>店舗情報掲載料</h3>
    <p>1ページ：21,000円／年額</p>
    <p>複数ページ：42,000円／年額<br>（写真・メニュー・クーポン等）</p>
    <p>求人情報掲載無料（採用時31,500円）</p>
    <div class="contact">
      <p>連絡先</p>
      <p>TEL：096-XXX-XXXX</p>
      <p>info@semu.ro.jp</p>
    </div>
  </div>
</section>

<section class="about">
  <h2>ーセム</h2>
  <p>《選ぶワクワクを全ての人に》をミッションにしたNPOです。この度開設するサイトを通じて、大人の生活の選択肢を増やし、学習支援によって子どもの将来の選択肢を増やすことを目的としています。</p>
  <p class="address">〒123-4567<br>熊本県XXXX-XXXXX</p>
</section>

<section class="screens">
  <div class="screen" role="img" aria-label="サイトのトップページ画面" style="left:0;top:0;width:268px;height:150px;background:linear-gradient(180deg,#fbe3c0,#f4f4f4)"></div>
  <div class="screen" role="img" aria-label="店舗ページ画面" style="left:0;top:162px;width:128px;height:156px;background:linear-gradient(180deg,#f7d9c8,#f2f2f2)"></div>
  <div class="screen" role="img" aria-label="グルメ特集画面" style="left:140px;top:162px;width:128px;height:156px;background:linear-gradient(180deg,#f4c46a,#efe8dc)"></div>
</section>

<div class="footer"></div>
</body>
</html>
```